CALDERWYN STATIONARY
CALDRWYN STATIONARY
CALDERWYN STATIONARY -
Creative Brief
Professional
KHALID R AL-MUTAWA
CEO
P.O.BOX: 57384 RIYADH: 12958 KINGDOM OF SAUDI ARABIA
kalmutawa@mailvero.com
www.calderwyn-example.com

```html
<!DOCTYPE html>
<html lang="en">
<head>
<meta charset="utf-8">
<title>Calderwyn Stationery – Business Cards</title>
<link href="https://fonts.googleapis.com/css2?family=Open+Sans:wght@400;600;700&display=swap" rel="stylesheet">
<style>
  :root {
    --bg: #e9e6e1;
    --card: #ffffff;
    --gold: #c9952e;
    --gold-light: #e8c877;
    --gold-dark: #9c6d18;
    --name: #d08a2a;
    --blue: #1f4e96;
    --navy: #17306a;
    --ink: #4a4a4a;
    --rule: #cfcfcf;
  }
  * { margin: 0; padding: 0; box-sizing: border-box; }
  html, body { width: 1200px; height: 852px; overflow: hidden; }
  body {
    background: var(--bg);
    font-family: "Open Sans", Arial, sans-serif;
    position: relative;
  }
  .card {
    position: absolute;
    width: 540px; height: 310px;
    background: var(--card);
    border-radius: 16px;
    overflow: hidden;
    box-shadow: 0 6px 18px rgba(0,0,0,.18);
  }
  .card--left-logo { left: 50px; top: 70px; }
  .card--center-logo { left: 610px; top: 470px; }

  .brand-square {
    position: absolute;
    width: 40px; height: 40px;
    background: linear-gradient(135deg, var(--gold-light), var(--gold) 55%, var(--gold-dark));
  }
  .brand-name {
    position: absolute;
    font-weight: 700;
    font-size: 30px;
    letter-spacing: 1px;
    color: var(--gold);
    line-height: 1;
  }
  .tagline {
    position: absolute;
    font-weight: 700;
    font-size: 10.5px;
    color: var(--blue);
    letter-spacing: .3px;
    white-space: nowrap;
  }
  .person-name {
    position: absolute;
    font-weight: 700;
    font-size: 15px;
    color: var(--name);
    white-space: nowrap;
  }
  .person-role {
    position: absolute;
    font-weight: 600;
    font-size: 11px;
    color: var(--gold-dark);
  }
  .address {
    position: absolute;
    font-size: 10.5px;
    line-height: 15px;
    color: var(--ink);
    white-space: nowrap;
  }
  .divider {
    position: absolute;
    width: 1px;
    background: var(--rule);
  }
  .contacts {
    position: absolute;
    list-style: none;
    font-size: 10.5px;
    color: var(--ink);
  }
  .contacts li {
    display: flex; align-items: center;
    height: 18px;
    white-space: nowrap;
  }
  .contacts svg { width: 12px; height: 12px; margin-right: 7px; flex: none; }
  .wave { position: absolute; left: 0; bottom: 0; width: 540px; height: 90px; }

  /* left-logo card */
  .card--left-logo .brand-square { left: 40px; top: 32px; }
  .card--left-logo .brand-name { left: 92px; top: 33px; }
  .card--left-logo .tagline { left: 92px; top: 66px; }
  .card--left-logo .person-name { right: 290px; top: 118px; text-align: right; }
  .card--left-logo .person-role { right: 290px; top: 140px; }
  .card--left-logo .address { right: 290px; top: 170px; text-align: right; }
  .card--left-logo .divider { left: 268px; top: 112px; height: 118px; }
  .card--left-logo .contacts { left: 284px; top: 112px; }

  /* center-logo card */
  .card--center-logo .brand-square { left: 115px; top: 80px; width: 50px; height: 50px; }
  .card--center-logo .brand-name { left: 40px; top: 146px; width: 200px; text-align: center; }
  .card--center-logo .tagline { left: 40px; top: 180px; width: 200px; text-align: center; font-size: 9.5px; }
  .card--center-logo .person-name { left: 292px; top: 34px; }
  .card--center-logo .person-role { left: 292px; top: 56px; }
  .card--center-logo .address { left: 292px; top: 80px; }
  .card--center-logo .divider { left: 276px; top: 36px; height: 196px; }
  .card--center-logo .contacts { left: 292px; top: 128px; }
</style>
</head>
<body>

<svg width="0" height="0" style="position:absolute" aria-hidden="true">
  <defs>
    <linearGradient id="goldBand" x1="0" y1="0" x2="1" y2="0">
      <stop offset="0" stop-color="#b07c1e"/>
      <stop offset=".45" stop-color="#f0d58e"/>
      <stop offset="1" stop-color="#b8862a"/>
    </linearGradient>
    <symbol id="icon-phone" viewBox="0 0 12 12">
      <path d="M3 1.5l1.6 2.2-1 1a6 6 0 0 0 3.7 3.7l1-1L10.5 9 9.3 10.5C5 10.2 1.8 7 1.5 2.7z" fill="#c9952e"/>
    </symbol>
    <symbol id="icon-mobile" viewBox="0 0 12 12">
      <rect x="3.5" y="1" width="5" height="10" rx="1" fill="#c9952e"/>
      <rect x="4.5" y="2.2" width="3" height="6" fill="#fff"/>
    </symbol>
    <symbol id="icon-fax" viewBox="0 0 12 12">
      <rect x="1.5" y="4.5" width="9" height="5.5" rx="1" fill="#c9952e"/>
      <rect x="3.5" y="1.5" width="5" height="3" fill="#c9952e"/>
    </symbol>
    <symbol id="icon-mail" viewBox="0 0 12 12">
      <circle cx="6" cy="6" r="5.5" fill="#c9952e"/>
      <rect x="3" y="4" width="6" height="4" fill="#fff"/>
      <path d="M3 4l3 2.2L9 4" stroke="#c9952e" stroke-width=".8" fill="none"/>
    </symbol>
    <symbol id="icon-web" viewBox="0 0 12 12">
      <circle cx="6" cy="6" r="5.5" fill="#c9952e"/>
      <ellipse cx="6" cy="6" rx="2.2" ry="4.5" stroke="#fff" stroke-width=".8" fill="none"/>
      <path d="M1.5 6h9" stroke="#fff" stroke-width=".8"/>
    </symbol>
    <symbol id="card-wave" viewBox="0 0 540 90" preserveAspectRatio="none">
      <path d="M0 40 C150 25 320 30 540 8 L540 14 C320 38 150 34 0 48 Z" fill="#17306a"/>
      <path d="M0 52 C160 40 330 44 540 22 L540 90 L0 90 Z" fill="url(#goldBand)"/>
    </symbol>
  </defs>
</svg>

<section class="card card--left-logo">
  <div class="brand-square"></div>
  <div class="brand-name">CALDERWYN</div>
  <div class="tagline">YOUR CAPITAL RESTS ON FIRM GROUND</div>

  <div class="person-name">KHALID R AL-MUTAWA</div>
  <div class="person-role">CEO</div>
  <div class="address">P.O.BOX: 57384<br>RIYADH: 12958<br>KINGDOM OF SAUDI ARABIA</div>

  <div class="divider"></div>
  <ul class="contacts">
    <li><svg><use href="#icon-phone"/></svg>920001234</li>
    <li><svg><use href="#icon-phone"/></svg>+966 1 400 1234</li>
    <li><svg><use href="#icon-mobile"/></svg>+966 55 000 2468</li>
    <li><svg><use href="#icon-fax"/></svg>+966 1 400 5678</li>
    <li><svg><use href="#icon-mail"/></svg>kalmutawa@mailvero.com</li>
    <li><svg><use href="#icon-web"/></svg>www.calderwyn-example.com</li>
  </ul>

  <svg class="wave" viewBox="0 0 540 90" preserveAspectRatio="none" aria-hidden="true"><use href="#card-wave"/></svg>
</section>

<section class="card card--center-logo">
  <div class="brand-square"></div>
  <div class="brand-name">CALDERWYN</div>
  <div class="tagline">YOUR CAPITAL RESTS ON FIRM GROUND</div>

  <div class="divider"></div>
  <div class="person-name">KHALID R AL-MUTAWA</div>
  <div class="person-role">CEO</div>
  <div class="address">P.O.BOX: 57384<br>RIYADH: 12958<br>KINGDOM OF SAUDI ARABIA</div>

  <ul class="contacts">
    <li><svg><use href="#icon-phone"/></svg>920001234</li>
    <li><svg><use href="#icon-phone"/></svg>+966 1 400 1234</li>
    <li><svg><use href="#icon-mobile"/></svg>+966 55 000 2468</li>
    <li><svg><use href="#icon-fax"/></svg>+966 1 400 5678</li>
    <li><svg><use href="#icon-mail"/></svg>kalmutawa@mailvero.com</li>
    <li><svg><use href="#icon-web"/></svg>www.calderwyn-example.com</li>
  </ul>

  <svg class="wave" viewBox="0 0 540 90" preserveAspectRatio="none" aria-hidden="true"><use href="#card-wave"/></svg>
</section>

</body>
</html>
```